Start up needs juice bottle label design

Bramblecrest Citrus Co juice company needs juice bottle label design for all natural lemonades, teas, smoothies and cold-pressed juice. We would like the design to have a space for multiple flavors or custom recipes for special orders. Below is the company logo.

Target Market(s)

On-the-go Health conscious

```html
<!DOCTYPE html>
<html lang="en">
<head>
<meta charset="utf-8">
<title>Bramblecrest Citrus Co — Cold Pressed Juice Labels</title>
<link href="https://fonts.googleapis.com/css2?family=Amatic+SC:wght@400;700&family=Caveat:wght@500&display=swap" rel="stylesheet">
<style>
  :root {
    --strawberry-bg: #b52226;
    --strawberry-label-a: #d0282c;
    --strawberry-label-b: #b52226;
    --strawberry-art: #a91d22;
    --orange-bg: #ef8429;
    --orange-label-a: #f6982c;
    --orange-label-b: #f0852a;
    --orange-art: #e27620;
    --ink: #111111;
    --paper: #ffffff;
  }
  * { margin: 0; padding: 0; box-sizing: border-box; }
  html, body { width: 1200px; height: 1200px; overflow: hidden; }
  body { display: flex; font-family: "Amatic SC", cursive; }
  .panel { position: relative; width: 600px; height: 1200px; }
  .panel--strawberry { background: var(--strawberry-bg); }
  .panel--orange { background: var(--orange-bg); }

  .label {
    position: absolute; left: 137px; top: 194px;
    width: 326px; height: 812px; border-radius: 6px;
    box-shadow: 4px 6px 10px rgba(0,0,0,0.35);
    color: var(--paper);
  }
  .label--strawberry { background: linear-gradient(135deg, var(--strawberry-label-a), var(--strawberry-label-b)); }
  .label--orange { background: linear-gradient(135deg, var(--orange-label-a), var(--orange-label-b)); }

  .brand {
    position: absolute; left: 0; right: 0; top: 48px;
    text-align: center; font-weight: 700; font-size: 46px; line-height: 1;
    color: var(--paper);
  }

  .tag {
    position: absolute; background: var(--ink); color: var(--paper);
    font-weight: 700; text-align: center; line-height: 1;
  }
  .tag--cold { left: 25px; top: 168px; width: 272px; height: 78px; font-size: 58px; padding-top: 8px; transform: rotate(-0.4deg); }
  .tag--juice { left: 93px; top: 248px; width: 140px; height: 80px; font-size: 58px; padding-top: 9px; transform: rotate(-0.8deg); }

  .fruit-art {
    position: absolute; left: 49px; top: 356px; width: 208px; height: 177px;
    border-radius: 40% 40% 30% 30%;
  }
  .label--strawberry .fruit-art { background: var(--strawberry-art); }
  .label--orange .fruit-art { background: var(--orange-art); }

  .flavor {
    position: absolute; left: 0; right: 0; top: 555px;
    text-align: center; font-size: 46px; font-weight: 400; line-height: 1; letter-spacing: 1px;
  }
  .claim {
    position: absolute; left: 0; right: 0; top: 612px;
    text-align: center; font-size: 26px; line-height: 1; font-weight: 400;
  }
  .promise {
    position: absolute; left: 40px; right: 40px; top: 650px;
    display: flex; align-items: center; justify-content: space-between;
    font-size: 40px; line-height: 1;
  }
  .promise__badge { width: 62px; height: 62px; }
  .volume {
    position: absolute; left: 117px; top: 733px; width: 95px; height: 52px;
    background: var(--ink); color: var(--paper); border-radius: 3px;
    font-family: "Caveat", cursive; font-size: 30px; line-height: 50px; text-align: center;
  }
</style>
</head>
<body>
  <section class="panel panel--strawberry">
    <article class="label label--strawberry">
      <div class="brand">Bramblecrest Citrus Co</div>
      <div class="tag tag--cold">COLD PRESSED</div>
      <div class="tag tag--juice">JUICE</div>
      <div class="fruit-art" role="img" aria-label="White line drawing of a strawberry with hearts and juice splashes"></div>
      <h2 class="flavor">STRAWBERRY JUICE</h2>
      <p class="claim">NO SUGAR ADDED</p>
      <div class="promise">
        <span>FRESH</span>
        <svg class="promise__badge" viewBox="0 0 62 62" aria-hidden="true">
          <circle cx="31" cy="31" r="27" fill="none" stroke="#fff" stroke-width="4"/>
          <path d="M30 45 C18 42 15 30 17 20 C26 24 31 33 30 45Z" fill="#fff"/>
          <path d="M32 45 C44 42 47 30 45 18 C36 23 31 33 32 45Z" fill="#fff"/>
        </svg>
        <span>NATURAL</span>
      </div>
      <div class="volume">473mL</div>
    </article>
  </section>
  <section class="panel panel--orange">
    <article class="label label--orange">
      <div class="brand">Bramblecrest Citrus Co</div>
      <div class="tag tag--cold">COLD PRESSED</div>
      <div class="tag tag--juice">JUICE</div>
      <div class="fruit-art" role="img" aria-label="White line drawing of an orange slice with hearts and juice splashes"></div>
      <h2 class="flavor">ORANGE JUICE</h2>
      <p class="claim">NO SUGAR ADDED</p>
      <div class="promise">
        <span>FRESH</span>
        <svg class="promise__badge" viewBox="0 0 62 62" aria-hidden="true">
          <circle cx="31" cy="31" r="27" fill="none" stroke="#fff" stroke-width="4"/>
          <path d="M30 45 C18 42 15 30 17 20 C26 24 31 33 30 45Z" fill="#fff"/>
          <path d="M32 45 C44 42 47 30 45 18 C36 23 31 33 32 45Z" fill="#fff"/>
        </svg>
        <span>NATURAL</span>
      </div>
      <div class="volume">473mL</div>
    </article>
  </section>
</body>
</html>
```